Website redesign

Redesign the Website

http://www.trauringe-kolbeck.de/

Task

- make 1 Layout for the Website
- Colors: white, yellow, brown
- Text: Take from Page - ore rather Use Latin - Lore Ipsum ...
- pimp design and overall look
- enhance overview for better orientation
- more freindly / sympatic overall look.
- Better integrate Palvista Button aso.
- send Layout as layered PSD

```html
<!DOCTYPE html>
<html lang="de">
<head>
<meta charset="utf-8">
<title>Trauringe Kolbeck – Solitairringe</title>
<link rel="stylesheet" href="https://fonts.googleapis.com/css2?family=Cormorant+Garamond:wght@500;700&family=Open+Sans:wght@400;600;700&display=swap">
<style>
:root{
  --gold:#d8a21c;
  --brown:#6b4a1c;
  --text:#3a3a3a;
  --muted:#8a8a8a;
  --line:#e4e4e4;
  --white:#ffffff;
  --footer:#0d0d0d;
  --footer-text:#9b9b9b;
  --contact-bg:#f4f4f4;
}
*{margin:0;padding:0;box-sizing:border-box}
html,body{width:1200px;height:2624px;overflow:hidden;background:var(--white)}
body{position:relative;font-family:"Open Sans",Arial,sans-serif;color:var(--text)}

.site-header{position:absolute;top:0;left:0;width:1200px;height:230px;border-bottom:1px solid var(--line)}
.brand{position:absolute;left:0;top:58px;width:1200px;text-align:center;font-family:"Open Sans",Arial,sans-serif;font-weight:600;font-size:34px;color:var(--brown);line-height:1}
.social{position:absolute;right:116px;top:64px;display:flex;align-items:center;gap:10px;font-size:18px;font-weight:600;color:var(--text)}
.social-box{width:36px;height:36px;background:var(--text);border-radius:4px}
.main-nav{position:absolute;top:180px;left:100px;width:1000px;display:flex;justify-content:space-between;font-size:17px;color:var(--muted)}
.main-nav a{color:inherit;text-decoration:none;padding:0 14px}
.main-nav .active{color:var(--brown);font-weight:600}

.hero{position:absolute;top:248px;left:0;width:1200px;height:424px;background:linear-gradient(90deg,#f3ead9 0%,#fbf7ef 45%,#f2eadb 100%);border-bottom:6px solid var(--gold)}
.hero-rings{position:absolute;left:0;top:0;width:340px;height:418px;background:radial-gradient(circle at 50% 55%,#f6d779 0%,#d39a22 45%,#a77214 75%,#ede2cc 100%)}
.hero-bride{position:absolute;right:0;top:0;width:400px;height:418px;background:linear-gradient(160deg,#efe7dc 0%,#e9c7c8 35%,#f7f4ef 65%,#c9b9a6 100%)}
.hero-text{position:absolute;left:380px;top:140px;color:var(--brown)}
.hero-text .l1{font-family:"Cormorant Garamond",Georgia,serif;font-weight:700;font-size:40px;line-height:1.05}
.hero-text .l2{font-family:"Cormorant Garamond",Georgia,serif;font-weight:700;font-size:40px}
.hero-text .l2 b{color:var(--gold);font-size:64px}
.hero-text .l3{font-family:"Cormorant Garamond",Georgia,serif;font-size:30px;margin-left:170px}

.about{position:absolute;top:712px;left:100px;width:1000px;text-align:center}
.section-title{font-family:"Cormorant Garamond",Georgia,serif;font-weight:700;font-size:34px;color:var(--text)}
.about p{margin-top:18px;font-size:15px;line-height:1.6;color:var(--muted);text-align:left}

.edition{position:absolute;left:100px;width:1000px}
.edition .section-title{text-align:center}
.pager{position:absolute;right:0;top:8px;font-size:16px;color:var(--muted);display:flex;gap:8px;align-items:center}
.pager .current{color:var(--gold);font-weight:700}
.ring-row{margin-top:30px;display:grid;grid-template-columns:repeat(5,1fr);gap:16px}
.ring{text-align:center}
.ring-photo{height:140px;margin:0 auto;width:160px;border-radius:6px}
.gold{background:radial-gradient(ellipse at 50% 55%,#fbe6a2 0%,#e0ac2b 45%,#fff 80%)}
.white{background:radial-gradient(ellipse at 50% 55%,#ffffff 0%,#c8c8c8 45%,#fff 80%)}
.rose{background:radial-gradient(ellipse at 50% 55%,#f4c9a6 0%,#d8895a 40%,#ccc 60%,#fff 82%)}
.bicolor{background:radial-gradient(ellipse at 40% 55%,#e8b445 0%,#d0d0d0 50%,#fff 82%)}
.ring-code{margin-top:10px;font-size:14px;color:var(--text)}
.ring-code .alloy{color:var(--gold);font-weight:600}
.ring-stone{font-size:13px;color:var(--muted)}

.video{position:absolute;top:2000px;left:140px;width:908px;height:272px;background:linear-gradient(135deg,#3b332b 0%,#8b7a66 45%,#cdbca6 70%,#4a3f35 100%)}
.video-title{position:absolute;left:0;top:0;width:100%;height:46px;background:rgba(0,0,0,.55);color:#fff;font-size:17px;padding:12px 18px}
.video-play{position:absolute;left:424px;top:110px;width:60px;height:60px;border-radius:50%;background:rgba(0,0,0,.7)}
.video-play svg{position:absolute;left:22px;top:18px}

.contact-bar{position:absolute;top:2296px;left:0;width:1200px;height:56px;background:var(--contact-bg);display:flex;justify-content:center;gap:90px;align-items:center;font-size:19px;color:var(--text)}

.site-footer{position:absolute;top:2360px;left:0;width:1200px;height:264px;background:var(--footer)}
.footer-photo{position:absolute;left:0;top:0;width:440px;height:264px;background:radial-gradient(circle at 45% 45%,#5a4a2c 0%,#231d14 35%,#0d0d0d 70%)}
.footer-links{position:absolute;left:600px;top:40px;display:flex;gap:50px;font-size:13px;line-height:1.75;color:var(--footer-text)}
.footer-links ul{list-style:none}
.footer-bottom{position:absolute;left:600px;top:218px;font-size:12px;color:#6f6f6f}
</style>
</head>
<body>

<header class="site-header">
  <div class="brand">Trauringe Kolbeck</div>
  <div class="social"><span class="social-box"></span>Palvista</div>
  <nav class="main-nav">
    <a href="#">Wedding Rings</a>
    <a href="#" class="active">Solitairings</a>
    <a href="#">Partner rings</a>
    <a href="#">Bridal Jewelry</a>
    <a href="#">Information</a>
    <a href="#">Contact</a>
  </nav>
</header>

<section class="hero">
  <div class="hero-rings" role="img" aria-label="Golden diamond wedding rings close-up"></div>
  <div class="hero-bride" role="img" aria-label="Bride holding a bouquet of pink and white roses"></div>
  <div class="hero-text">
    <div class="l1">The most</div>
    <div class="l2">beautiful <b>wedding</b> ...</div>
    <div class="l3">a life long</div>
  </div>
</section>

<section class="about">
  <h2 class="section-title">About Us</h2>
  <p>Lorem Ipsum is simply dummy text of the printing and typesetting industry. Lorem Ipsum is simply dummy text of the printing and typesetting industry. Lorem Ipsum is simply dummy text of the printing and typesetting industry. Lorem Ipsum is simply dummy text of the printing and typesetting industry. Lorem Ipsum is simply dummy text of the printing and typesetting industry.</p>
</section>

<section class="edition" style="top:884px">
  <h2 class="section-title">Edition 1</h2>
  <div class="pager">Page: <span class="current">1</span><span>2</span><span>3</span><span>&rarr;</span></div>
  <div class="ring-row">
    <div class="ring"><div class="ring-photo gold" role="img" aria-label="Pair of yellow gold rings"></div><div class="ring-code">718/6 <span class="alloy">Gelbgold</span></div><div class="ring-stone">1 Brillant 0,05 Carat</div></div>
    <div class="ring"><div class="ring-photo white" role="img" aria-label="Pair of white gold rings"></div><div class="ring-code">41108/6 Weißgold</div><div class="ring-stone">5 Brillanten 0,09 Carat</div></div>
    <div class="ring"><div class="ring-photo white" role="img" aria-label="Pair of white gold rings with stones"></div><div class="ring-code">41126/6 Weißgold</div><div class="ring-stone">5 Brillanten 0,09 Carat</div></div>
    <div class="ring"><div class="ring-photo rose" role="img" aria-label="Pair of rose and white gold rings"></div><div class="ring-code">41352/6 Weißgold</div><div class="ring-stone">16 Brillanten 0,16 Carat</div></div>
    <div class="ring"><div class="ring-photo bicolor" role="img" aria-label="Pair of bicolour gold rings"></div><div class="ring-code">41270/4.5 Weißgold</div><div class="ring-stone">1 Brillant 0,03 Carat</div></div>
  </div>
</section>

<section class="edition" style="top:1196px">
  <h2 class="section-title">Edition 2</h2>
  <div class="pager">Page: <span class="current">1</span><span>2</span><span>3</span><span>&rarr;</span></div>
  <div class="ring-row">
    <div class="ring"><div class="ring-photo rose" role="img" aria-label="Pair of rose gold rings"></div><div class="ring-code">718/6 <span class="alloy">Gelbgold</span></div><div class="ring-stone">1 Brillant 0,05 Carat</div></div>
    <div class="ring"><div class="ring-photo gold" role="img" aria-label="Pair of yellow gold rings"></div><div class="ring-code">41108/6 Weißgold</div><div class="ring-stone">5 Brillanten 0,09 Carat</div></div>
    <div class="ring"><div class="ring-photo gold" role="img" aria-label="Pair of yellow gold rings"></div><div class="ring-code">41126/6 Weißgold</div><div class="ring-stone">5 Brillanten 0,09 Carat</div></div>
    <div class="ring"><div class="ring-photo white" role="img" aria-label="Pair of white gold rings"></div><div class="ring-code">41352/6 Weißgold</div><div class="ring-stone">16 Brillanten 0,16 Carat</div></div>
    <div class="ring"><div class="ring-photo gold" role="img" aria-label="Pair of yellow gold rings"></div><div class="ring-code">41270/4.5 Weißgold</div><div class="ring-stone">1 Brillant 0,03 Carat</div></div>
  </div>
</section>

<section class="edition" style="top:1520px">
  <h2 class="section-title">Edition 3</h2>
  <div class="pager">Page: <span class="current">1</span><span>2</span><span>3</span><span>&rarr;</span></div>
  <div class="ring-row">
    <div class="ring"><div class="ring-photo bicolor" role="img" aria-label="Pair of bicolour rings"></div><div class="ring-code">41126/6 Weißgold</div><div class="ring-stone">5 Brillanten 0,09 Carat</div></div>
    <div class="ring"><div class="ring-photo rose" role="img" aria-label="Pair of rose gold rings"></div><div class="ring-code">718/6 <span class="alloy">Gelbgold</span></div><div class="ring-stone">1 Brillant 0,05 Carat</div></div>
    <div class="ring"><div class="ring-photo gold" role="img" aria-label="Pair of yellow gold rings"></div><div class="ring-code">41270/4.5 Weißgold</div><div class="ring-stone">1 Brillant 0,03 Carat</div></div>
    <div class="ring"><div class="ring-photo gold" role="img" aria-label="Pair of yellow gold rings"></div><div class="ring-code">41108/6 Weißgold</div><div class="ring-stone">5 Brillanten 0,09 Carat</div></div>
    <div class="ring"><div class="ring-photo white" role="img" aria-label="Pair of white gold rings"></div><div class="ring-code">41108/6 Weißgold</div><div class="ring-stone">5 Brillanten 0,09 Carat</div></div>
  </div>
</section>

<section class="video" role="img" aria-label="Video still of hands holding a pair of wedding rings">
  <div class="video-title">Der Wunsch Eures Lebens: Neue Eheringe</div>
  <div class="video-play"><svg width="20" height="24" viewBox="0 0 20 24"><polygon points="0,0 20,12 0,24" fill="#fff"/></svg></div>
</section>

<div class="contact-bar">
  <span>Tel: 0821-447310</span>
  <span>Fax: 0821-447315</span>
  <span>mail@trauringe-kolbeck.de</span>
</div>

<footer class="site-footer">
  <div class="footer-photo" role="img" aria-label="Gold rings on a dark reflective surface"></div>
  <div class="footer-links">
    <ul><li>Trauringe Kolbeck</li><li>Edition 1</li><li>Edition 2</li><li>Solitaire</li></ul>
    <ul><li>Fair Edition</li><li>Preisliste</li><li>Über uns</li><li>Kontakt</li></ul>
    <ul><li>Ringgrößen</li><li>Schmuck Pflege</li><li>Werkstatt</li><li>Impressum</li></ul>
  </div>
  <div class="footer-bottom">Trauringe Kolbeck GmbH · Lindenweg 14 · 86150 Augsburg</div>
</footer>

</body>
</html>
```